Harborlight Energy Local Letter Drop

I need a compelling and visually appealing flyer to promote our solar installation company in our local area of Boronia Victoria.
Because we are an install company without the overheads of the big solar sales companies, we pride ourselves on being the experts and being able to provide great quality service and products at the best prices anywhere.
In a highly competitive market we need to convey that despite government incentives and feed-in tariff rates being reduced by the government, solar has never been more affordable or economical for families. This is due to the significant fall in solar equipment prices, but this is set to change as international manufacturers start to go out of business. With electricity/utility prices set to rise even further, solar is a perfect option for domestic and commercial use.
I want a leaflet that is grabbing and compels people to ring me for a free, no obligation quotation and in-home energy assessment.
We want to differentiate ourselves from the stand-point of cutting out the middle man and being the local, trusted and expert installers.
We want to protect people from the projected 60% rise in electricity prices over the coming 8 years and allow them to produce their own electricity!

```html
<!DOCTYPE html>
<html lang="en">
<head>
<meta charset="utf-8">
<title>Harborlight Energy – The Solar Panel Installers</title>
<link href="https://fonts.googleapis.com/css2?family=Black+Ops+One&family=Lato:wght@400;700&family=Open+Sans:wght@400;600&family=Tinos:wght@400;700&display=swap" rel="stylesheet">
<style>
  :root {
    --page-grey: #6f6f6f;
    --ink-dark: #1b0d0d;
    --ink-deep: #0e0606;
    --band-dark: #261414;
    --gold: #f6c21c;
    --gold-deep: #e8a90f;
    --white: #ffffff;
    --silver-light: #eeeeee;
    --silver-dark: #9a9a9a;
    --text-black: #111111;
  }
  * { box-sizing: border-box; margin: 0; padding: 0; }
  html, body { width: 945px; height: 1200px; overflow: hidden; }
  body { background: var(--page-grey); font-family: "Lato", Arial, sans-serif; position: relative; }

  .flyer {
    position: absolute; left: 25px; top: 15px; width: 895px; height: 1158px; overflow: hidden;
    background: radial-gradient(ellipse at 50% 18%, #3a1a1a 0%, var(--ink-dark) 45%, var(--ink-deep) 100%);
  }

  .brand-badge {
    position: absolute; left: 283px; top: -180px; width: 330px; height: 338px;
    border-radius: 50%; background: var(--white); border: 3px solid var(--gold-deep);
  }
  .brand-name {
    position: absolute; left: 283px; top: 84px; width: 330px; text-align: center;
    font-family: "Lato", Arial, sans-serif; font-weight: 700; font-size: 26px; color: #2a2a2a;
  }

  .contact-email { position: absolute; left: 24px; top: 40px; font-family: Arial, sans-serif; font-size: 17px; }
  .contact-email .label { color: var(--gold); display: block; font-size: 18px; }
  .contact-email a { color: var(--white); text-decoration: none; }
  .contact-phone {
    position: absolute; right: 22px; top: 40px; color: var(--white);
    font-family: Arial, sans-serif; font-size: 17px; display: flex; align-items: center; gap: 4px;
  }

  .headline, .closing {
    position: absolute; left: 0; width: 895px; text-align: center; white-space: nowrap;
    font-family: "Black Ops One", Impact, sans-serif; font-weight: 400;
    background: linear-gradient(180deg, var(--silver-light) 0%, #d6d6d6 50%, var(--silver-dark) 100%);
    -webkit-background-clip: text; background-clip: text; color: transparent;
  }
  .headline { top: 160px; font-size: 52px; line-height: 60px; letter-spacing: 1px; }
  .closing { top: 1038px; font-size: 47px; line-height: 56px; letter-spacing: 0; }

  .hero-photo {
    position: absolute; left: 25px; top: 240px; width: 408px; height: 284px;
    border: 8px solid var(--gold);
    background: linear-gradient(180deg, #2d6fd0 0%, #5a98e6 45%, #b5643c 70%, #8e3d1f 100%);
  }
  .hero-arrows { position: absolute; left: 430px; top: 240px; }

  .questions { position: absolute; left: 459px; top: 248px; list-style: none; }
  .questions li {
    font-family: Arial, Helvetica, sans-serif; font-size: 29px; line-height: 38px; color: var(--gold);
    margin-bottom: 20px; width: 400px;
  }

  .promise-band {
    position: absolute; left: 0; top: 547px; width: 895px; height: 44px;
    background: repeating-linear-gradient(135deg, var(--band-dark) 0 3px, #1d0f0f 3px 6px);
  }
  .promise {
    position: absolute; left: 0; top: 550px; width: 895px; text-align: center; white-space: nowrap;
    font-family: "Open Sans", Arial, sans-serif; font-size: 28px; color: var(--gold);
  }

  .intro {
    position: absolute; left: 28px; top: 597px; width: 840px; color: var(--white);
    font-size: 18px; line-height: 24px; text-align: justify;
  }
  .intro p + p { margin-top: 20px; }
  .intro .call-number { font-size: 22px; font-family: Arial, sans-serif; }

  .data-strip { position: absolute; left: 0; top: 750px; }

  .chart-card {
    position: absolute; left: 47px; top: 785px; width: 250px; height: 222px;
    background: var(--white); box-shadow: 2px 3px 8px rgba(0,0,0,0.45);
  }

  .price-card {
    position: absolute; left: 470px; top: 788px; width: 382px; height: 218px;
    background: var(--white); box-shadow: 2px 3px 8px rgba(0,0,0,0.45); padding: 8px 7px 0;
    font-family: "Tinos", "Times New Roman", serif; color: var(--text-black);
  }
  .price-table { width: 368px; border-collapse: collapse; table-layout: fixed; font-size: 16px; }
  .price-table th, .price-table td { border: 1px solid var(--text-black); padding: 2px 6px; }
  .price-table th { height: 44px; text-align: center; font-weight: 700; line-height: 18px; }
  .price-table td { height: 47px; text-align: center; line-height: 18px; }
  .price-table td.payback { text-align: left; }
  .col-kw { width: 80px; } .col-price { width: 88px; } .col-off { width: 92px; } .col-pay { width: 108px; }
  .price-note { text-align: center; font-size: 11px; margin-top: 4px; white-space: nowrap; }

  .address {
    position: absolute; left: 0; top: 1113px; width: 895px; text-align: center;
    font-family: Arial, sans-serif; font-size: 20px; color: var(--gold-deep);
  }
</style>
</head>
<body>
<main class="flyer">
  <div class="brand-badge"></div>
  <div class="brand-name">Harborlight Energy</div>

  <div class="contact-email">
    <span class="label">Email:</span>
    <a href="mailto:hello@harborlightenergy.com.au">hello@harborlightenergy.com.au</a>
  </div>
  <div class="contact-phone">
    <svg width="18" height="18" viewBox="0 0 18 18" aria-hidden="true">
      <circle cx="9" cy="9" r="9" fill="#f6c21c"/>
      <path d="M6 4.5c-.8.4-1.4 1.5-1 3 .6 2.4 2.8 5 5 5.8 1.3.5 2.3.1 2.8-.6l-1.6-1.6-1.2.6c-1.1-.5-2.1-1.6-2.6-2.7l.7-1.2z" fill="#1b0d0d"/>
    </svg>
    <span>1300 555 019</span>
  </div>

  <h1 class="headline">The Solar Panel Installers</h1>

  <div class="hero-photo" role="img" aria-label="Installer in an orange shirt laying solar panels on a terracotta tiled roof under a blue sky"></div>
  <svg class="hero-arrows" width="30" height="290" viewBox="0 0 30 290" aria-hidden="true">
    <polygon points="0,20 14,34 0,48" fill="#f6c21c"/>
    <polygon points="0,118 14,132 0,146" fill="#f6c21c"/>
    <polygon points="0,216 14,230 0,244" fill="#f6c21c"/>
  </svg>

  <ul class="questions">
    <li>Have You Thought About Solar?</li>
    <li>Are you paying too much for electricity?</li>
    <li>Would you like to reduce or even eliminate your bills?</li>
  </ul>

  <div class="promise-band"></div>
  <p class="promise">........ then as your local solar installer, we can help you!</p>

  <div class="intro">
    <p>In the past six years, electricity prices have gone up by more than 93% and are due to increase even further! We have helped thousands of households avoid electricity price hikes….and they have been incredibly happy with the savings. Now we would like to pass these savings on to you.</p>
    <p>As your local installer we would like to offer you a free, no obligation quote and energy assessment to see how solar can work for you, give us a call today on <span class="call-number">1300 555 019</span></p>
  </div>

  <svg class="data-strip" width="895" height="300" viewBox="0 0 895 300" aria-hidden="true">
    <polygon fill="#ffffff" points="0,18 30,12 55,20 90,8 120,16 160,6 200,17 240,10 280,19 320,7 360,15 400,9 440,18 480,6 520,14 560,10 600,19 640,8 680,16 720,11 760,18 800,7 840,15 870,10 895,16 895,282 860,290 820,279 780,288 740,280 700,291 660,281 620,289 580,279 540,288 500,280 460,290 420,281 380,288 340,279 300,289 260,280 220,290 180,281 140,288 100,279 60,289 30,281 0,288"/>
  </svg>

  <div class="chart-card">
    <svg width="250" height="222" viewBox="0 0 250 222" role="img" aria-label="Bar chart of quarterly electricity bill projections from 2004 to 2022">
      <defs>
        <linearGradient id="barFill" x1="0" y1="0" x2="0" y2="1">
          <stop offset="0" stop-color="#f4a3a0"/>
          <stop offset="1" stop-color="#d9403c"/>
        </linearGradient>
      </defs>
      <text x="10" y="20" font-family="Arial, sans-serif" font-size="12.5" font-weight="700" fill="#333">Quarterly Electricity Bill Projections</text>
      <g font-family="Arial, sans-serif" font-size="8" fill="#333" text-anchor="end">
        <text x="36" y="42">$1,400</text><text x="36" y="62">$1,200</text><text x="36" y="82">$1,000</text>
        <text x="36" y="102">$800</text><text x="36" y="122">$600</text><text x="36" y="142">$400</text>
        <text x="36" y="162">$200</text><text x="36" y="182">$-</text>
      </g>
      <g stroke="#dddddd" stroke-width="0.8">
        <line x1="40" y1="39" x2="242" y2="39"/><line x1="40" y1="59" x2="242" y2="59"/><line x1="40" y1="79" x2="242" y2="79"/>
        <line x1="40" y1="99" x2="242" y2="99"/><line x1="40" y1="119" x2="242" y2="119"/><line x1="40" y1="139" x2="242" y2="139"/>
        <line x1="40" y1="159" x2="242" y2="159"/>
      </g>
      <line x1="40" y1="179" x2="242" y2="179" stroke="#888" stroke-width="1"/>
      <g fill="url(#barFill)">
        <rect x="46" y="147" width="12" height="32"/>
        <rect x="66" y="138" width="12" height="41"/>
        <rect x="86" y="130" width="12" height="49"/>
        <rect x="106" y="122" width="12" height="57"/>
        <rect x="126" y="113" width="12" height="66"/>
        <rect x="146" y="105" width="12" height="74"/>
        <rect x="166" y="96" width="12" height="83"/>
        <rect x="186" y="88" width="12" height="91"/>
        <rect x="206" y="80" width="12" height="99"/>
        <rect x="226" y="62" width="12" height="117"/>
      </g>
      <g font-family="Arial, sans-serif" font-size="8" fill="#333" text-anchor="end">
        <text transform="translate(56,186) rotate(-45)">2004</text>
        <text transform="translate(76,186) rotate(-45)">2006</text>
        <text transform="translate(96,186) rotate(-45)">2008</text>
        <text transform="translate(116,186) rotate(-45)">2010</text>
        <text transform="translate(136,186) rotate(-45)">2012</text>
        <text transform="translate(156,186) rotate(-45)">2014</text>
        <text transform="translate(176,186) rotate(-45)">2016</text>
        <text transform="translate(196,186) rotate(-45)">2018</text>
        <text transform="translate(216,186) rotate(-45)">2020</text>
        <text transform="translate(236,186) rotate(-45)">2022</text>
      </g>
    </svg>
  </div>

  <div class="price-card">
    <table class="price-table">
      <colgroup><col class="col-kw"><col class="col-price"><col class="col-off"><col class="col-pay"></colgroup>
      <thead>
        <tr><th>KW</th><th>PRICE</th><th>% off bill</th><th>Pay Back Period</th></tr>
      </thead>
      <tbody>
        <tr><td>1.5</td><td>$1650</td><td>35%</td><td class="payback">2 years 10 months</td></tr>
        <tr><td>3</td><td>$4300</td><td>71%</td><td class="payback">3 years 7 months</td></tr>
        <tr><td>5</td><td>$7000</td><td>100%</td><td class="payback">4 years 2 months</td></tr>
      </tbody>
    </table>
    <p class="price-note">Figures based on average household energy usage of 17kws/day</p>
  </div>

  <h2 class="closing">Start enjoying your savings today!</h2>
  <p class="address">42 Lanternfield Drive, Boronia Vic 3155</p>
</main>
</body>
</html>
```